Business Card For Talent Company
BLITZ Talent
Project: Business Card For Talent Company
Business Card For Talent Company - Entertainment
Creative Brief
Cutting-Edge
Lorna Pidge
Talent Development
2734 W. Ferncastle Rd. Dovermill Park IL 60419
blitztalent@quorvex.com
www.blitztalent-quorvex.com
Are you ready to break through?
Kelvorn Kelvorn
We are really desperate to see some fun contemporary and modern designs...we are a talent company...would really like to see something innovative and not so corporate looking.....thank you!
Aquamarine/Teal Shade of Blue Please!....We really want something fun and edgy....these are too corporate looking...
We are a talent agency....really looking for something cool and cutting edge for our company...the shade of blue is coming through wrong on the logo...we are looking for a more like a teal blue color....thank you!
Our Tag Line "are you ready to break through" needs to be on all of the materials....thank you!
we are looking for more of teal shade of blue..I uploaded our other logo....
This contest is for full stationary...
It is both business card and stationary that we are needing....thank you!

```html
<!DOCTYPE html>
<html lang="en">
<head>
<meta charset="utf-8">
<title>BLITZ Talent — Stationery</title>
<link rel="stylesheet" href="https://fonts.googleapis.com/css2?family=Michroma&family=Open+Sans:wght@400;600&display=swap">
<style>
  :root {
    --bg: #2b2b2b;
    --paper: #ffffff;
    --ink: #111214;
    --ink-soft: #5d6166;
    --teal: #17b5e6;
    --teal-deep: #0b86c4;
    --folder: #0c0c0d;
    --folder-mark: #3a3d40;
  }
  * { box-sizing: border-box; margin: 0; padding: 0; }
  html, body { width: 1200px; height: 869px; overflow: hidden; }
  body { background: var(--bg); font-family: "Open Sans", sans-serif; color: var(--ink); position: relative; }

  .piece { position: absolute; overflow: hidden; box-shadow: 0 6px 18px rgba(0,0,0,.45); }
  .piece svg.swoosh { position: absolute; left: 0; width: 100%; height: 100%; top: 0; }

  .wordmark { font-family: "Michroma", sans-serif; font-weight: 400; letter-spacing: 1px; white-space: nowrap; position: absolute; }
  .wordmark.on-light { color: var(--ink); }
  .wordmark.on-dark { color: var(--paper); }

  .tagline { font-family: "Open Sans", sans-serif; color: var(--teal); position: absolute; white-space: nowrap; }
  .fine { font-size: 6.5px; color: var(--ink-soft); position: absolute; white-space: nowrap; line-height: 1.5; }

  /* letterhead */
  .letterhead { left: 40px; top: 50px; width: 300px; height: 424px; background: var(--paper); }
  .letterhead .wordmark { right: 22px; top: 24px; font-size: 14px; }
  .letterhead .fine { left: 22px; bottom: 18px; color: var(--paper); }

  /* folder */
  .folder { left: 370px; top: 50px; width: 300px; height: 424px; background: var(--folder); }
  .folder .wordmark { left: 0; right: 0; text-align: center; top: 170px; font-size: 24px; color: var(--folder-mark); }
  .folder .tagline { left: 0; right: 0; text-align: center; top: 212px; font-size: 12px; color: var(--teal-deep); }

  /* business cards */
  .card { width: 320px; height: 183px; }
  .card-front { left: 720px; top: 50px; background: var(--paper); }
  .card-front .wordmark { left: 22px; top: 22px; font-size: 15px; }
  .card-front .person { position: absolute; left: 22px; top: 62px; }
  .card-front .person .name { font-weight: 600; font-size: 11px; }
  .card-front .person .role { font-size: 8px; color: var(--ink-soft); }
  .card-front .fine { left: 22px; top: 96px; font-size: 7px; }

  .card-back { left: 720px; top: 253px; background: var(--ink); }
  .card-back .wordmark { left: 0; right: 0; text-align: center; top: 66px; font-size: 18px; }
  .card-back .tagline { left: 0; right: 0; text-align: center; top: 100px; font-size: 9px; }

  /* envelopes */
  .envelope { width: 360px; height: 180px; background: var(--paper); }
  .envelope-front { left: 40px; top: 540px; }
  .envelope-front .wordmark { left: 20px; top: 18px; font-size: 11px; }
  .envelope-front .fine { left: 20px; top: 40px; }
  .envelope-back { left: 420px; top: 540px; }
  .envelope-back .wordmark { left: 0; right: 0; text-align: center; top: 48px; font-size: 13px; }
  .envelope-back .tagline { left: 0; right: 0; text-align: center; top: 72px; font-size: 8px; }

  /* note card */
  .notecard { left: 800px; top: 500px; width: 360px; height: 210px; background: var(--paper); }
  .notecard .wordmark { right: 24px; top: 22px; font-size: 14px; }
  .notecard .tagline { right: 24px; top: 44px; font-size: 8px; color: var(--teal-deep); }
</style>
</head>
<body>
<svg width="0" height="0" style="position:absolute">
  <defs>
    <linearGradient id="teal-band" x1="0" y1="0" x2="1" y2="0">
      <stop offset="0" stop-color="#0b86c4"/>
      <stop offset="1" stop-color="#2fd0f2"/>
    </linearGradient>
  </defs>
</svg>

<section class="piece letterhead">
  <svg class="swoosh" viewBox="0 0 300 424" preserveAspectRatio="none" aria-hidden="true">
    <path d="M0 340 C90 380 200 400 300 394 L300 424 L0 424 Z" fill="url(#teal-band)"/>
    <path d="M0 372 C90 404 200 416 300 412 L300 424 L0 424 Z" fill="var(--ink)"/>
  </svg>
  <div class="wordmark on-light">BLITZ Talent</div>
  <div class="fine">2734 W. Ferncastle Rd. Dovermill Park IL 60419 · www.blitztalent-quorvex.com</div>
</section>

<section class="piece folder">
  <div class="wordmark">BLITZ Talent</div>
  <div class="tagline">Are you ready to break through?</div>
</section>

<section class="piece card card-front">
  <svg class="swoosh" viewBox="0 0 320 183" preserveAspectRatio="none" aria-hidden="true">
    <path d="M0 140 C110 170 220 150 320 96 L320 183 L0 183 Z" fill="url(#teal-band)"/>
    <path d="M0 166 C120 186 230 160 320 124 L320 183 L0 183 Z" fill="var(--ink)"/>
  </svg>
  <div class="wordmark on-light">BLITZ Talent</div>
  <div class="person">
    <div class="name">Lorna Pidge</div>
    <div class="role">Talent Development</div>
  </div>
  <div class="fine">2734 W. Ferncastle Rd. Dovermill Park IL 60419<br>blitztalent@quorvex.com<br>www.blitztalent-quorvex.com</div>
</section>

<section class="piece card card-back">
  <svg class="swoosh" viewBox="0 0 320 183" preserveAspectRatio="none" aria-hidden="true">
    <path d="M0 0 L320 0 L320 26 C220 10 110 20 0 44 Z" fill="url(#teal-band)"/>
  </svg>
  <div class="wordmark on-dark">BLITZ Talent</div>
  <div class="tagline">Are you ready to break through?</div>
</section>

<section class="piece envelope envelope-front">
  <svg class="swoosh" viewBox="0 0 360 180" preserveAspectRatio="none" aria-hidden="true">
    <path d="M0 150 C120 172 250 160 360 130 L360 180 L0 180 Z" fill="url(#teal-band)"/>
  </svg>
  <div class="wordmark on-light">BLITZ Talent</div>
  <div class="fine">2734 W. Ferncastle Rd.<br>Dovermill Park IL 60419</div>
</section>

<section class="piece envelope envelope-back">
  <svg class="swoosh" viewBox="0 0 360 180" preserveAspectRatio="none" aria-hidden="true">
    <path d="M0 0 L360 0 L360 30 C300 110 230 128 180 128 C130 128 60 110 0 30 Z" fill="var(--ink)"/>
    <path d="M0 30 C60 110 130 128 180 128 C230 128 300 110 360 30 L360 40 C300 120 230 136 180 136 C130 136 60 120 0 40 Z" fill="url(#teal-band)"/>
  </svg>
  <div class="wordmark on-dark">BLITZ Talent</div>
  <div class="tagline">Are you ready to break through?</div>
</section>

<section class="piece notecard">
  <svg class="swoosh" viewBox="0 0 360 210" preserveAspectRatio="none" aria-hidden="true">
    <path d="M0 120 C90 160 220 180 360 176 L360 210 L0 210 Z" fill="url(#teal-band)"/>
  </svg>
  <div class="wordmark on-light">BLITZ Talent</div>
  <div class="tagline">Are you ready to break through?</div>
</section>
</body>
</html>
```